Design an Exhibition Poster for our Web Application

Our company develops and sells VaultLarkly, a web-based service that helps small businesses to test their web applications for security vulnerabilities.

You can see details of the service at the following page:

https://www.vaultlarkly.example/

We need a poster designed, to be used on an exhibition stand at a professional security conference.

Reason: The deadline for this project is being extended because we have, so far, received very few design submissions and they are generally not of the aesthetic quality we are looking for.

Target Market(s)

Tech startups and small / medium sized online businesses

Industry/Entity Type

Security

Requirements
Must have
• [1] Incorporate the VaultLarkly logo (see attached file).

[2] Use the text supplied by us (see attached file).

[3] Use a color scheme that matches the scheme used on our website.

[4] Project the visual theme of cyber security (or protection against cyber crime).
Nice to have
• This is part of a 2-poster set. The project for designing the other poster in the set is also being listed on ArtHivePlace today. Please look for the project entitled "Design an Exhibition Poster for our Software Product".

Preference will be given to designers who submit a pair of designs that harmonize with each other.

```html
<!DOCTYPE html>
<html lang="en">
<head>
<meta charset="utf-8">
<title>VaultLarkly Exhibition Poster – Options</title>
<link rel="stylesheet" href="https://fonts.googleapis.com/css2?family=Arimo:wght@400;700&display=swap">
<style>
  :root {
    --green: #acc567;
    --green-strong: #8dbb2a;
    --ink: #111111;
    --grey-text: #7d7d7d;
    --logo-grey: #8a8a8a;
    --frame: #c8c8c8;
    --pink: #e6007e;
    --deco-light: #e2e2e2;
    --deco-mid: #6f7376;
    --deco-dark: #3e4447;
    --dot: #55595c;
    --footer-top: #4a4a4a;
    --footer-bottom: #0e0e0e;
  }
  * { box-sizing: border-box; margin: 0; padding: 0; }
  html, body { width: 1200px; height: 831px; overflow: hidden; background: #ffffff; }
  body { position: relative; font-family: "Arimo", Arial, sans-serif; color: var(--ink); }

  .swatch { position: absolute; left: 42px; top: 12px; width: 90px; height: 24px; background: var(--green); }
  .swatch-label { position: absolute; left: 140px; top: 11px; font-size: 22px; line-height: 26px; }

  .option-number {
    position: absolute; top: 64px; width: 21px; height: 21px; border-radius: 50%;
    background: var(--pink); color: #fff; font-size: 13px; line-height: 21px; text-align: center;
  }

  .poster {
    position: absolute; top: 63px; width: 553px; height: 763px;
    border: 1px solid var(--frame);
    background: linear-gradient(#ffffff 0%, #fafafa 40%, #ececec 70%);
    overflow: hidden; text-align: center;
  }

  .poster-backdrop {
    position: absolute; left: 0; right: 0; top: 545px; height: 155px;
    background: linear-gradient(180deg, var(--deco-light) 0%, var(--deco-mid) 55%, var(--deco-dark) 100%);
  }

  .brand {
    position: absolute; top: 82px; left: 0; right: 0;
    display: flex; justify-content: center; align-items: center; gap: 20px;
  }
  .brand-mark { width: 58px; height: 58px; background: var(--green); }
  .brand-name { font-size: 50px; font-weight: 700; color: var(--logo-grey); letter-spacing: 0.5px; }

  .headline {
    position: absolute; left: 0; right: 0;
    font-size: 30px; font-weight: 700; color: var(--green); letter-spacing: 0.3px;
  }
  .intro { position: absolute; left: 0; right: 0; font-size: 16px; line-height: 19px; color: var(--ink); }

  .benefit-list { position: absolute; left: 0; right: 0; list-style: none; font-size: 14px; line-height: 18px; color: var(--grey-text); }
  .benefit-list li { margin-bottom: 4px; }
  .benefit-list .dot {
    display: inline-block; width: 9px; height: 9px; border-radius: 50%;
    background: var(--dot); margin-right: 4px;
  }
  .benefit-label { color: var(--green-strong); font-weight: 700; }

  .benefit-stack { position: absolute; left: 0; right: 0; }
  .benefit-stack h3 { font-size: 20px; line-height: 24px; font-weight: 700; color: var(--green-strong); }
  .benefit-stack p { font-size: 14px; line-height: 18px; color: var(--grey-text); margin-bottom: 17px; }

  .footer {
    position: absolute; left: 0; right: 0; bottom: 0; height: 62px;
    border-top: 4px solid var(--green);
    background: linear-gradient(var(--footer-top), var(--footer-bottom));
    color: #ffffff;
  }
  .footer-url { display: block; margin-top: 6px; font-size: 20px; font-weight: 700; line-height: 24px; }
  .footer-cta { display: block; font-size: 14px; line-height: 18px; }
</style>
</head>
<body>
  <div class="swatch"></div>
  <div class="swatch-label">#acc567</div>

  <div class="option-number" style="left:10px;">1</div>
  <section class="poster" style="left:40px;">
    <div class="poster-backdrop" role="img" aria-label="Abstract angular grey and green geometric backdrop"></div>
    <div class="brand"><span class="brand-mark"></span><span class="brand-name">VaultLarkly</span></div>
    <h1 class="headline" style="top:276px;">SECURITY FOR WEB STARTUPS</h1>
    <p class="intro" style="top:328px;">Online website vulnerability scanning that tells you exactly<br>what needs fixing and how to to fix it.</p>
    <ul class="benefit-list" style="top:392px;">
      <li><span class="dot"></span><span class="benefit-label">Accessible</span>: VaultLarkly runs in the cloud and is accessible<br>from any computer, anywhere, any time.</li>
      <li><span class="dot"></span><span class="benefit-label">Affordable:</span> VaultLarkly uses a flexible pay-as-you-go<br>model that will fit any budget.</li>
      <li><span class="dot"></span><span class="benefit-label">Simple</span>: Launch your scan using a simple 3-step wizard and we'll do the rest.</li>
    </ul>
    <footer class="footer">
      <span class="footer-url">www.vaultlarkly.example</span>
      <span class="footer-cta">TRY IT FREE TODAY!</span>
    </footer>
  </section>

  <div class="option-number" style="left:608px;">2</div>
  <section class="poster" style="left:636px;">
    <div class="poster-backdrop" role="img" aria-label="Abstract angular grey and green geometric backdrop"></div>
    <div class="brand"><span class="brand-mark"></span><span class="brand-name">VaultLarkly</span></div>
    <h1 class="headline" style="top:227px;">SECURITY FOR WEB STARTUPS</h1>
    <p class="intro" style="top:266px;">Online website vulnerability scanning that tells you exactly<br>what needs fixing and how to to fix it.</p>
    <div class="benefit-stack" style="top:327px;">
      <h3>Accessible:</h3>
      <p>VaultLarkly runs in the cloud and is accessible<br>from any computer, anywhere, any time.</p>
      <h3>Affordable:</h3>
      <p>VaultLarkly uses a flexible pay-as-you-go<br>model that will fit any budget.</p>
      <h3>Simple:</h3>
      <p style="line-height:22px;">Launch your scan using a simple 3-step<br>wizard and we'll do the rest.</p>
    </div>
    <footer class="footer">
      <span class="footer-url">www.vaultlarkly.example</span>
      <span class="footer-cta">TRY IT FREE TODAY!</span>
    </footer>
  </section>
</body>
</html>
```